Halloway Crest Backers Guild business cards

Create a single-sided business card for the Halloway Crest Backers Guild based on the attached logo.
The additional data fields include Name, Title, Email, Phone, and website.
Please use the following as sample data:
Name: Dean Varrow
Title: Co-Founder / Investor
Email: deanvarrow@mailtern.net
Phone: 555-314-2706
Website: www.hcbackersguild.com

Target Market(s)

Start ups, entrepreneurs, venture capitalists

Industry/Entity Type

Investment

Contact Information for Business Card

Professional business card. Technology company.

Font styles to use
Serif
Sans Serif

Requirements
Must have
• Include the HCBG logo (attached)
• Name
• Title
• Email
• Phone
• Website
Should not have
• Cute, cartoony

```html
<!DOCTYPE html>
<html lang="en">
<head>
<meta charset="utf-8">
<title>Halloway Crest Backers Guild — Business Card</title>
<link href="https://fonts.googleapis.com/css2?family=Open+Sans:wght@400;600;700&display=swap" rel="stylesheet">
<style>
  :root {
    --page-bg: #e9e9e7;
    --card-bg: #fbfbfa;
    --brand-green: #2fae72;
    --brand-green-soft: #5cc394;
    --ink-dark: #3d3d3d;
    --ink-mid: #5a5a5a;
    --ink-light: #7a7a7a;
  }
  * { margin: 0; padding: 0; box-sizing: border-box; }
  html, body {
    width: 1200px;
    height: 1022px;
    overflow: hidden;
    background: var(--page-bg);
    font-family: "Open Sans", Arial, sans-serif;
  }
  .business-card {
    position: absolute;
    left: 100px;
    top: 225px;
    width: 1000px;
    height: 572px;
    background: var(--card-bg);
    box-shadow: 0 6px 24px rgba(0,0,0,0.12);
  }
  .brand-circle {
    position: absolute;
    left: 150px;
    top: 186px;
    width: 200px;
    height: 200px;
    border-radius: 50%;
    background: var(--brand-green-soft);
  }
  .brand-name {
    position: absolute;
    left: 520px;
    top: 92px;
    font-size: 44px;
    line-height: 50px;
    font-weight: 600;
    color: var(--ink-mid);
    letter-spacing: 0.5px;
  }
  .divider {
    position: absolute;
    left: 330px;
    top: 212px;
    width: 560px;
    height: 3px;
    background: linear-gradient(to right, rgba(47,174,114,0), var(--brand-green) 35%);
  }
  .contact-block {
    position: absolute;
    left: 520px;
    top: 236px;
  }
  .person-name {
    font-size: 36px;
    font-weight: 700;
    color: var(--brand-green);
    line-height: 46px;
  }
  .person-title {
    font-size: 27px;
    font-weight: 400;
    color: var(--ink-mid);
    line-height: 40px;
    margin-bottom: 18px;
  }
  .contact-list { list-style: none; }
  .contact-item {
    display: flex;
    align-items: center;
    gap: 16px;
    font-size: 26px;
    line-height: 40px;
    color: var(--ink-dark);
  }
  .contact-item.is-bold { font-weight: 600; }
  .contact-icon { width: 20px; height: 20px; flex: none; }
  .web-domain { color: var(--brand-green); }
</style>
</head>
<body>
  <section class="business-card">
    <div class="brand-circle"></div>
    <div class="brand-name">Halloway Crest<br>Backers Guild</div>
    <div class="divider"></div>

    <div class="contact-block">
      <p class="person-name">Dean Varrow</p>
      <p class="person-title">Co-Founder / Investor</p>
      <ul class="contact-list">
        <li class="contact-item is-bold">
          <svg class="contact-icon" viewBox="0 0 20 20" aria-hidden="true">
            <path d="M5 2 L8 2 L9 6 L7 8 Q9 12 12 13 L14 11 L18 12 L18 15 Q17 18 14 18 Q4 16 2 5 Q2 2 5 2 Z" fill="var(--brand-green)"/>
          </svg>
          <span>555-314-2706</span>
        </li>
        <li class="contact-item">
          <svg class="contact-icon" viewBox="0 0 20 20" aria-hidden="true">
            <rect x="2" y="4" width="16" height="12" fill="none" stroke="var(--brand-green)" stroke-width="2"/>
            <path d="M2 4 L10 11 L18 4" fill="none" stroke="var(--brand-green)" stroke-width="2"/>
          </svg>
          <span>deanvarrow@mailtern.net</span>
        </li>
        <li class="contact-item is-bold">
          <svg class="contact-icon" viewBox="0 0 20 20" aria-hidden="true">
            <circle cx="10" cy="10" r="8" fill="none" stroke="var(--brand-green)" stroke-width="2"/>
            <path d="M2 10 H18 M10 2 Q5 10 10 18 M10 2 Q15 10 10 18" fill="none" stroke="var(--brand-green)" stroke-width="1.5"/>
          </svg>
          <span>www.<span class="web-domain">hcbackersguild.com</span></span>
        </li>
      </ul>
    </div>
  </section>
</body>
</html>
```